Business Card Need to Update Services

I need my business cards updated to include my correct headquarters address, local office, and telephon: Leadershipervices are Leadership Development, eLearning, Diversity Equity, Inclusion and Belonging Consultant Speaker, Management Consulting, Leadership Assessment and Devment, Governance and Compliance, Small Business Consulting. My Company is Halvorn Busines Services, LLC, I have two platforms Corvell Unity 24/7 services only Diversity, Equity, Inclusion and Business Serves or face to face human resource development services and training , Corvell Unity Learning and elearning plataform where individuals can purchase learning material,Use a clean and professional design that reflects your brand identity. Incorporate your company logo and choose colors that align with your branding.
Include your updated headquarters address, local office address, and telephone number prominently on the card.
Use a legible font for your name, job title, and contact information.
Consider adding a tagline that succinctly conveys your core services. For example, "Leadership Development | eLearning | DEI Consulting."

Target Market(s)

CEO and Leaders

Industry/Entity Type

Business Consulting and Business Services

Contact Information for Business Card

The services I provide, qr code that is not statistic, business certification

Requirements
Must have
• My contact information, my services and be representative of my company www.corvellunity247.example, Corvell Unity Learning, Pronouns|She|Hers, both address headquarters 5271 West Marlowe Pkwy Ste 614 Dallas, Texas 79341 and other location 743 Pine Hollow Blvd. Glenn Heights, Texas 79862
Nice to have
• my certification icons , SBE (Small Business Enterprise) MBE (Minority Business Enterprise) WOSB, Women owned small business,
Should not have
• Rude and disrepectful terms

```html
<!DOCTYPE html>
<html lang="en">
<head>
<meta charset="utf-8">
<title>Halvorn Business Services – Business Cards</title>
<link rel="stylesheet" href="https://fonts.googleapis.com/css2?family=Open+Sans:wght@400;600;700&display=swap">
<style>
  :root {
    --navy: #27306e;
    --ink: #3a3a3a;
    --grey: #8a8a8a;
    --paper: #ffffff;
    --backdrop: #dcdcda;
  }
  * { box-sizing: border-box; margin: 0; padding: 0; }
  html, body { width: 1200px; height: 801px; overflow: hidden; }
  body {
    background: var(--backdrop);
    font-family: "Open Sans", Arial, sans-serif;
    display: flex;
    align-items: center;
    justify-content: center;
    gap: 36px;
  }
  .card {
    position: relative;
    width: 560px;
    height: 320px;
    background: var(--paper);
    border-radius: 18px;
    border-bottom: 3px solid var(--navy);
    border-left: 2px solid var(--navy);
    overflow: hidden;
    box-shadow: 0 6px 18px rgba(0,0,0,.18);
  }

  /* Shared brand lockup */
  .brand { display: flex; align-items: center; gap: 12px; }
  .brand-mark { width: 18px; height: 18px; background: var(--navy); flex: none; }
  .brand-rule { width: 1px; align-self: stretch; background: var(--grey); }
  .brand-name {
    color: var(--navy);
    font-weight: 700;
    font-size: 22px;
    letter-spacing: 3px;
    text-transform: uppercase;
    line-height: 1.15;
  }
  .brand-name small { display: block; font-size: 10px; letter-spacing: 2.5px; }

  /* Contact side */
  .card-contact .brand { position: absolute; top: 30px; left: 34px; height: 46px; }
  .qr-code {
    position: absolute; top: 24px; right: 34px;
    width: 74px; height: 74px;
    border: 2px solid var(--navy);
    background: #eef0f6;
  }
  .person { position: absolute; left: 34px; top: 108px; }
  .person-name { color: var(--navy); font-weight: 700; font-size: 20px; letter-spacing: .5px; line-height: 1.2; }
  .person-title { color: var(--ink); font-size: 13px; line-height: 1.4; }
  .person-pronouns { color: var(--grey); font-size: 11.5px; }
  .divider {
    position: absolute; left: 34px; right: 34px; top: 178px;
    height: 1.5px; background: var(--navy);
  }
  .contacts { position: absolute; left: 34px; top: 190px; list-style: none; }
  .contacts li {
    display: flex; align-items: center; gap: 8px;
    color: var(--ink); font-size: 12px; line-height: 22px;
  }
  .contacts svg { width: 11px; height: 11px; fill: var(--navy); flex: none; }
  .addresses {
    position: absolute; right: 34px; top: 190px;
    text-align: right; color: var(--ink); font-size: 11.5px; line-height: 16px;
  }
  .addresses dt { color: var(--navy); font-weight: 700; font-size: 10.5px; letter-spacing: .6px; text-transform: uppercase; }
  .addresses dd + dt { margin-top: 6px; }

  /* Brand side */
  .card-brand .brand { position: absolute; top: 74px; left: 44px; gap: 18px; height: 84px; }
  .card-brand .brand-mark { width: 30px; height: 30px; }
  .card-brand .brand-name { font-size: 42px; letter-spacing: 6px; }
  .card-brand .brand-name small { font-size: 14px; letter-spacing: 4px; margin-top: 4px; color: var(--ink); }
  .tagline-band {
    position: absolute; left: 0; right: 0; bottom: 34px;
    height: 32px; background: var(--navy);
    color: var(--paper); font-size: 15px; letter-spacing: .4px;
    display: flex; align-items: center; justify-content: center;
  }
</style>
</head>
<body>

  <section class="card card-contact">
    <div class="brand">
      <span class="brand-mark"></span>
      <span class="brand-rule"></span>
      <div class="brand-name">Halvorn<small>Business Services, LLC.</small></div>
    </div>

    <div class="qr-code" role="img" aria-label="QR code linking to the company website"></div>

    <div class="person">
      <p class="person-name">MARCUS ELLERY</p>
      <p class="person-title">Managing Director</p>
      <p class="person-pronouns">Pronouns | She | Hers</p>
    </div>

    <div class="divider"></div>

    <ul class="contacts">
      <li><svg viewBox="0 0 12 12"><path d="M2 1h3l1 3-1.5 1a6 6 0 0 0 2.5 2.5L8 6l3 1v3a1 1 0 0 1-1 1A9 9 0 0 1 1 2a1 1 0 0 1 1-1z"/></svg>123 456 789</li>
      <li><svg viewBox="0 0 12 12"><path d="M0 2h12v8H0zM1 3l5 3.5L11 3v-.2H1z" fill-rule="evenodd"/></svg>info@corvellunity247.example</li>
      <li><svg viewBox="0 0 12 12"><circle cx="6" cy="6" r="5.5"/></svg>www.corvellunity247.example</li>
      <li><svg viewBox="0 0 12 12"><path d="M1 2h10v7H1zM0 10h12v1H0z"/></svg>Corvell Unity Learning</li>
    </ul>

    <dl class="addresses">
      <dt>Headquarters</dt>
      <dd>5271 West Marlowe Pkwy Ste 614</dd>
      <dd>Dallas, Texas 79341</dd>
      <dt>Local Office</dt>
      <dd>743 Pine Hollow Blvd.</dd>
      <dd>Glenn Heights, Texas 79862</dd>
    </dl>
  </section>

  <section class="card card-brand">
    <div class="brand">
      <span class="brand-mark"></span>
      <span class="brand-rule"></span>
      <div class="brand-name">Halvorn<small>Business Services, LLC.</small></div>
    </div>
    <div class="tagline-band">Leadership Development | eLearning | DEI Consulting</div>
  </section>

</body>
</html>
```